Vela Norvina is a dietary supplement company and in need of label design for 4 products

label for 4 dietary supplement products :1- Biotin. Red bottle ( please see the picture attached, not the whole bottle is colored but rather its a white bottle with the upper part and lower part of the bottle colored)2- COQ10. Orange Bottle 3- Hair Skin Nail. Pink bottle 4- Probiotics. Green Bottle we like the label to:1- have a modern and sleek appearance with very limited graphics.2- have a transparent background( as the bottle is white )3- have the box with the supplement and ingredient to appear sideways( horizontal )4- to have a color matching the bottle color.attached you will find :1- the dimension of the bottle.2- four different labels for each of the products.3- two pictures of the bottles 4- picture of the caps5- Logo
Industry/Entity Type
Health And Wellness
Colors
Designer to choose colors to be used in the design.
Look and feel
Each slider illustrates characteristics of the customer's brand and the style your logo design should communicate.

```html
<!DOCTYPE html>
<html lang="en">
<head>
<meta charset="utf-8">
<title>Vela Norvina – Supplement Label Range</title>
<link href="https://fonts.googleapis.com/css2?family=Montserrat:wght@400;500;600;700&display=swap" rel="stylesheet">
<style>
  :root {
    --canvas: #f3f3f1;
    --label-white: #ffffff;
    --ink: #3a3a40;
    --ink-soft: #55555c;
    --biotin: #d7262e;
    --coq10: #f47a20;
    --hair: #e62ac0;
    --probiotic: #20a92f;
  }
  * { box-sizing: border-box; margin: 0; padding: 0; }
  html, body {
    width: 1200px; height: 622px; overflow: hidden;
    background: var(--canvas);
    font-family: "Montserrat", sans-serif;
    color: var(--ink);
  }
  .range { position: relative; width: 1200px; height: 622px; }

  .label {
    position: absolute; top: 140px; width: 168px; height: 365px;
    background: var(--label-white);
    border-radius: 6px 6px 22px 22px;
    box-shadow: 0 6px 18px rgba(0,0,0,.08);
    overflow: hidden;
  }
  .label--biotin { left: 155px; --accent: var(--biotin); }
  .label--coq10 { left: 371px; --accent: var(--coq10); }
  .label--hair { left: 590px; --accent: var(--hair); }
  .label--probiotic { left: 815px; --accent: var(--probiotic); }

  .band { position: absolute; top: 0; left: 0; width: 168px; height: 52px; }
  .band path { fill: var(--accent); }

  .brand {
    position: absolute; top: 72px; left: 0; width: 100%;
    display: flex; justify-content: center; align-items: center; gap: 5px;
    font-size: 11px; font-weight: 500; letter-spacing: .6px; color: var(--ink);
  }
  .brand-mark { width: 7px; height: 7px; background: var(--accent); }

  .title {
    position: absolute; left: 0; width: 100%; text-align: center;
    line-height: 1; white-space: nowrap;
  }
  .title--biotin {
    top: 142px; font-size: 35px; font-weight: 600; color: var(--biotin); letter-spacing: 1px;
  }
  .title--coq10 { top: 140px; font-size: 36px; font-weight: 700; color: var(--coq10); }
  .title--coq10 .num { color: var(--ink); font-weight: 500; }
  .title--hair {
    top: 136px; display: flex; justify-content: center; align-items: center; gap: 4px;
  }
  .title--hair .main { font-size: 33px; font-weight: 700; color: var(--hair); }
  .title--hair .side { font-size: 14px; font-weight: 500; color: var(--ink); line-height: 1; text-align: left; }
  .title--probiotic { top: 130px; line-height: .98; }
  .title--probiotic .row { display: block; font-size: 30px; font-weight: 700; color: var(--probiotic); }
  .title--probiotic .num { color: var(--ink); font-weight: 400; }
  .title--probiotic .count { display: block; font-size: 19px; font-weight: 400; color: var(--ink); margin-top: 2px; }

  .pattern {
    position: absolute; top: 187px; left: 6px; width: 156px; height: 56px;
    background: linear-gradient(90deg, transparent 0%, color-mix(in srgb, var(--accent) 16%, transparent) 30%, transparent 50%, color-mix(in srgb, var(--accent) 16%, transparent) 70%, transparent 100%);
  }
  .label--probiotic .pattern { top: 210px; }

  .badge {
    position: absolute; top: 190px; left: 58px; width: 53px; height: 53px;
    border-radius: 16px; background: var(--accent); color: #fff;
    display: flex; flex-direction: column; align-items: center; justify-content: center;
    line-height: .9;
  }
  .label--probiotic .badge { top: 213px; left: 56px; width: 57px; height: 57px; }
  .badge .sym { font-size: 27px; font-weight: 600; }
  .badge .sub { font-size: 12px; font-weight: 500; align-self: flex-end; margin-right: 8px; }
  .badge--stack .sym { font-size: 25px; font-weight: 700; }
  .badge--stack .sub { align-self: center; margin: 2px 0 0 14px; }

  .subtitle {
    position: absolute; top: 262px; left: 0; width: 100%; text-align: center;
    font-size: 13px; font-weight: 500; letter-spacing: 1px; color: var(--ink);
  }
  .label--hair .subtitle { top: 265px; }
  .tech { position: absolute; top: 281px; left: 0; width: 100%; text-align: center; line-height: 1.1; }
  .tech .name { display: block; font-size: 13px; font-weight: 600; letter-spacing: 1px; color: var(--ink); }
  .tech .name sup { font-size: 6px; font-weight: 500; vertical-align: top; margin-left: 1px; }
  .tech .by { display: block; font-size: 7px; font-weight: 500; letter-spacing: .5px; color: var(--ink-soft); }

  .count-tag {
    position: absolute; top: 306px; left: 14px; width: 140px; height: 22px;
    display: flex; border: 1px solid var(--ink-soft);
    white-space: nowrap; overflow: hidden;
  }
  .count-tag .qty {
    flex: 0 0 37px; background: var(--accent); color: #fff;
    display: flex; flex-direction: column; justify-content: center; padding-left: 4px;
  }
  .count-tag .qty b { font-size: 12px; font-weight: 700; line-height: 12px; }
  .count-tag .qty small { font-size: 4.3px; font-weight: 700; letter-spacing: .1px; line-height: 5px; }
  .count-tag .note {
    flex: 1; font-size: 6.6px; font-weight: 500; letter-spacing: .3px; line-height: 8px;
    display: flex; flex-direction: column; justify-content: center; padding-left: 6px; color: var(--ink);
  }
</style>
</head>
<body>
<main class="range">

  <article class="label label--biotin">
    <svg class="band" viewBox="0 0 168 52"><path d="M0 12 Q70 -6 168 14 L168 48 Q80 30 0 36 Z"/></svg>
    <div class="brand"><span class="brand-mark"></span><span>Vela Norvina</span></div>
    <h2 class="title title--biotin">BIOTIN</h2>
    <div class="pattern" role="img" aria-label="Geometric network line pattern in red"></div>
    <div class="badge"><span class="sym">B</span><span class="sub">7</span></div>
    <p class="subtitle">100%PURE</p>
    <div class="count-tag">
      <div class="qty"><b>60</b><small>CAPSULES</small></div>
      <div class="note"><span>PRIVATE LABELING</span><span>ANY CAPSULE COUNT</span></div>
    </div>
  </article>

  <article class="label label--coq10">
    <svg class="band" viewBox="0 0 168 52"><path d="M0 12 Q70 -6 168 14 L168 48 Q80 30 0 36 Z"/></svg>
    <div class="brand"><span class="brand-mark"></span><span>Vela Norvina</span></div>
    <h2 class="title title--coq10">COQ<span class="num">10</span></h2>
    <div class="pattern" role="img" aria-label="Geometric network line pattern in orange"></div>
    <div class="badge"><span class="sym">Q</span><span class="sub">10</span></div>
    <p class="subtitle">UBIQUINONE</p>
    <div class="count-tag">
      <div class="qty"><b>60</b><small>CAPSULES</small></div>
      <div class="note"><span>PRIVATE LABELING</span><span>ANY CAPSULE COUNT</span></div>
    </div>
  </article>

  <article class="label label--hair">
    <svg class="band" viewBox="0 0 168 52"><path d="M0 12 Q70 -6 168 14 L168 48 Q80 30 0 36 Z"/></svg>
    <div class="brand"><span class="brand-mark"></span><span>Vela Norvina</span></div>
    <h2 class="title title--hair"><span class="main">HAIR</span><span class="side">SKIN<br>&amp; NAILS</span></h2>
    <div class="pattern" role="img" aria-label="Geometric network line pattern in pink"></div>
    <div class="badge badge--stack"><span class="sym">V3</span><span class="sub">RO</span></div>
    <p class="subtitle">ESSENTIALS</p>
    <div class="count-tag">
      <div class="qty"><b>60</b><small>CAPSULES</small></div>
      <div class="note"><span>PRIVATE LABELING</span><span>ANY CAPSULE COUNT</span></div>
    </div>
  </article>

  <article class="label label--probiotic">
    <svg class="band" viewBox="0 0 168 52"><path d="M0 12 Q70 -6 168 14 L168 48 Q80 30 0 36 Z"/></svg>
    <div class="brand"><span class="brand-mark"></span><span>Vela Norvina</span></div>
    <h2 class="title title--probiotic">
      <span class="row">PRO<span class="num">40</span></span>
      <span class="row">BIOTIC</span>
      <span class="count">40 BILLION</span>
    </h2>
    <div class="pattern" role="img" aria-label="Geometric network line pattern in green"></div>
    <div class="badge badge--stack"><span class="sym">V6</span><span class="sub">RO</span></div>
    <p class="tech"><span class="name">ENTERSHIELD<sup>®</sup></span><span class="by">BY PASS TECHNOLOGY</span></p>
    <div class="count-tag">
      <div class="qty"><b>60</b><small>CAPSULES</small></div>
      <div class="note"><span>PRIVATE LABELING</span><span>ANY CAPSULE COUNT</span></div>
    </div>
  </article>

</main>
</body>
</html>
```